依頼概要
・依頼の目的/概要
人生100年時代に、認知症や介護予防・改善に役立つ、化粧療法レクレーションの表紙デザインをお願いします。

・本の内容
高齢者の皆さんを抱えた、娘さん世代、ソーシャルビジネスとして取り組みたい女性、人の役に立ちたい・介護や医療関係者のスキルアップとして、心を癒すスキンタッチケアとしての化粧療法レクレーションを知って頂き、その効果を実例等で理解する事で、実践してみたくなる内容にしています。またお仕事としても、ボランティアとしても活躍できるセラピストの役割や募集にもふれています。
化粧療法レクレーションがどんなものか?!やるとどんな効果がきたいできるのか?!に、研究データーと実際の実例を交えて説明・解説した本です。

・デザイン要望
美容で心が癒される事が、伝わるようなイメージと解説でもあるので、化粧療法レクレーションのバイブルみたいな感じでしょうか?!(イメージカラーは、ピンクです。http://tkvb.or.jp tkvb-sora.com 色の感じです、参考資料)
もちろん、デザイナーさんのセンスにお任せします。

その他何かご不明な点がございましたら、お気軽にご質問ください。
よろしくお願いいたします。
■ 選んだ理由

認知症や介護の予防・改善を目指した療法ですので、見た方が、明るく安心し、そして楽しみになるイメージが持てるデザインを選びました。特に当選したものは、高齢者と若者が一緒に映る写真の印象が、表題のレクレーションのイメージに繋がるということが、一番の選定理由です。

■ 提案者全員のお礼・コメント

素晴らしい表紙のデザインの応募をいただき、本当に感謝しています。
選定は、本当に悩みました。いくつも表紙にしたい作品がありました。出して頂いた作品が、教科書的と、読み物的な提案を頂いたように思います。皆さん素晴らしかったのですが、今回は親しみやすさを重視させて頂きました。特に最初に応募して頂いた、pelmiさんの表紙には、私の言いたい事が網羅されていて、良かったです。が、今回のテーマを考えて、残念ながら選定致しませんでした。
次の機会に皆様とお仕事ができれば、嬉しいです。ありがとうございました。

```html
<!DOCTYPE html>
<html lang="ja">
<head>
<meta charset="UTF-8">
<title>化粧療法レクレーション 表紙</title>
<link rel="stylesheet" href="https://fonts.googleapis.com/css2?family=M+PLUS+Rounded+1c:wght@500;800&family=Noto+Serif+JP:wght@700;900&display=swap">
<style>
  :root {
    --pink-band: #f7b3c2;
    --pink-soft: #fbd6de;
    --crimson: #c8163f;
    --rose: #e0467a;
    --ink: #2a1a1e;
    --white: #ffffff;
    --photo-top-a: #e9d7cf;
    --photo-top-b: #c9a89b;
    --photo-bottom-a: #e6e2de;
    --photo-bottom-b: #cfc2b8;
  }
  * { margin: 0; padding: 0; box-sizing: border-box; }
  html, body { width: 750px; height: 1200px; overflow: hidden; background: var(--white); }
  .cover {
    position: relative;
    width: 750px;
    height: 1200px;
    overflow: hidden;
    background: var(--white);
    font-family: "M PLUS Rounded 1c", sans-serif;
  }
  .hero-photo {
    position: absolute; left: 0; top: 0; width: 750px; height: 360px;
    background: linear-gradient(135deg, var(--photo-top-a) 0%, #f2e6df 45%, var(--photo-top-b) 100%);
  }
  .era-seal {
    position: absolute; left: 10px; top: -10px; width: 280px; height: 280px;
    border-radius: 50%; background: var(--white);
    display: flex; flex-direction: column; align-items: center; justify-content: center;
    font-family: "Noto Serif JP", serif; font-weight: 900; color: var(--crimson);
    line-height: 1.05; transform: rotate(-12deg);
  }
  .era-seal .line-a { font-size: 56px; }
  .era-seal .line-b { font-size: 64px; }
  .era-seal .line-c { font-size: 56px; }
  .method-badge {
    position: absolute; left: 470px; top: 190px; width: 200px; height: 150px;
    border-radius: 50%; background: var(--white);
    border: 5px solid var(--rose);
    display: flex; flex-direction: column; align-items: center; justify-content: center;
    font-family: "Noto Serif JP", serif; font-weight: 700; color: var(--crimson);
    font-size: 30px; line-height: 1.15; text-align: center; z-index: 2;
  }
  .method-badge .num { font-size: 40px; }
  .title-band {
    position: absolute; left: 0; top: 330px; width: 750px; height: 495px;
    background: linear-gradient(180deg, var(--pink-band) 0%, var(--pink-soft) 55%, var(--pink-band) 100%);
  }
  .subtitle {
    position: absolute; left: 0; top: 368px; width: 750px; text-align: center;
    font-weight: 800; font-size: 52px; line-height: 1.25; color: var(--crimson);
  }
  .main-title {
    position: absolute; left: 0; top: 510px; width: 750px; text-align: center;
    font-weight: 800; color: var(--crimson); line-height: 1.1;
  }
  .main-title .t1 { display: block; font-size: 88px; }
  .main-title .t2 { display: block; font-size: 92px; letter-spacing: -2px; }
  .author {
    position: absolute; left: 0; top: 730px; width: 750px; text-align: center;
    font-weight: 800; font-size: 24px; color: var(--ink);
  }
  .author .name { font-size: 34px; margin-left: 10px; }
  .portrait-photo {
    position: absolute; left: 0; top: 825px; width: 750px; height: 375px;
    background: linear-gradient(90deg, var(--photo-bottom-b) 0%, var(--photo-bottom-a) 35%, #f6f2ef 60%, #fde7ec 100%);
  }
  .closing-line {
    position: absolute; left: 370px; top: 880px; width: 370px; text-align: center;
    font-family: "Noto Serif JP", serif; font-weight: 700; color: var(--rose);
    font-size: 44px; line-height: 1.5;
  }
  .closing-line .big { font-size: 58px; }
</style>
</head>
<body>
<main class="cover">
  <div class="hero-photo" role="img" aria-label="笑顔の高齢女性と若い女性が寄り添う写真"></div>

  <div class="era-seal">
    <span class="line-a">人生</span>
    <span class="line-b">100年</span>
    <span class="line-c">時代!</span>
  </div>

  <div class="title-band"></div>

  <div class="method-badge">
    <span><span class="num">60</span>分で</span>
    <span>笑顔になれる</span>
    <span>メソッド</span>
  </div>

  <h2 class="subtitle">心を癒し、<br>健康寿命を延ばす</h2>

  <h1 class="main-title">
    <span class="t1">化粧療法</span>
    <span class="t2">レクレーション</span>
  </h1>

  <p class="author">全国ビューティーケア療法協会　代表理事<span class="name">森 早苗</span></p>

  <div class="portrait-photo" role="img" aria-label="白髪の高齢女性がほほえむ写真と花の飾り"></div>

  <p class="closing-line">
    <span class="big">人</span>生の最終章を<br>
    明るく、元気に<br>
    美しく
  </p>
</main>
</body>
</html>
```